Bayline Pet Rehoming GALA

Hi ALL!
We need an 8.5 X 11 inch, one page flyer to include all the below copy plus 8 sponsoring logos at the very bottom.
Thank YOU!

Corvel Heights Pet GALA
(Fun for Animals In Rescue!)

Sunday, August 12, 2018
1 to 4:30 p.m.

Animal Education & Adoption Event
featuring:

BK Pet Shelter & Services Rabbits & Mice

Hilltop Browsing Sheep

Thankful Hounds Haven

Featherwell Finches & Larks

Comet Pup Haven

Marla’s Feline Haven

Marvel Pup Haven

Special Guest from 1-3 p.m.
BeeBop - SF's 1st Therapy Pig!
Instagram: @BEEBOP_BKHOG
Facebook: @BEEBOP THE HOG

Activities for Kids
Dog & Cat Toy Making with Greta Vossel Canine Coaching
Animal Mask Making with Tiny Crafters
Face-in-a-Hole Photo Fun with Hugo Marsh Canine Coaching

BK PSS FREE Giveaway!
First 75 attending families receive a FREE PSS Doggie Bag containing a dog water bottle, food, shampoo, toy, treats and blinking dog collar light.

Animal Tails

1 pm Wendell’s Nook Storytime

1:30 p.m. BeeBop the Therapy Pig

1:45 pm “Tuft the Saved Hog”
Read by Author Marnie Oakhurst

2 p.m. Wendell’s Nook Singalong

2:30 p.m. Featherwell Finch Haven

2:45 p.m. Quire Pages Storytime

3 pm Browsing Sheep Refuge

3:15 p.m. The Burrow Den Puppet Show

3:45 pm BK PSS Officer Tamsin

4 p.m. Wendell’s Nook Storytime

Font styles to use
Serif

Colors

Designer to choose colors to be used in the design.

Requirements
Must have
• pig, goat, 2 dogs, kitten, dove, bunny

```html
<!DOCTYPE html>
<html lang="en">
<head>
<meta charset="utf-8">
<title>Corvel Heights Pet GALA</title>
<link rel="stylesheet" href="https://fonts.googleapis.com/css2?family=Kaushan+Script&family=Lato:wght@400;700;900&display=swap">
<style>
  :root {
    --stage: #1d1e22;
    --paper: #f4f4f6;
    --purple-deep: #1f1660;
    --purple-mid: #3a1f86;
    --purple-glow: #6a2fae;
    --orange: #f7941d;
    --ink: #2b2b30;
    --rule: #3a3a3f;
    --muted: #bcbcc2;
    --white: #ffffff;
  }
  * { margin: 0; padding: 0; box-sizing: border-box; }
  html, body { width: 1200px; height: 848px; overflow: hidden; background: var(--stage); }
  .canvas { position: relative; width: 1200px; height: 848px; }
  .flyer {
    position: absolute; left: 291px; top: 24px; width: 618px; height: 800px;
    background: var(--paper); overflow: hidden;
    font-family: "Lato", sans-serif; color: var(--ink);
  }
  .hero {
    position: absolute; left: 0; top: 0; width: 618px; height: 310px;
    background: radial-gradient(ellipse at 55% 70%, var(--purple-glow) 0%, var(--purple-mid) 45%, var(--purple-deep) 100%);
  }
  .schedule-panel {
    position: absolute; left: 330px; top: 300px; width: 288px; height: 400px;
    background: linear-gradient(180deg, var(--purple-mid) 0%, var(--purple-glow) 55%, var(--purple-mid) 100%);
    border-radius: 0 0 0 28px;
  }
  .accent-stripe { position: absolute; background: var(--orange); }
  .accent-stripe.left { left: 0; top: 306px; width: 330px; height: 5px; }
  .accent-stripe.right { left: 600px; top: 392px; width: 18px; height: 9px; }
  .title {
    position: absolute; left: 50px; top: 26px; color: var(--white);
    font-weight: 900; line-height: 0.98; letter-spacing: 0.5px;
  }
  .title .line-one { display: block; font-size: 44px; padding-left: 34px; }
  .title .line-two { display: block; font-size: 58px; }
  .tagline {
    position: absolute; left: 130px; top: 150px; width: 290px;
    font-family: "Kaushan Script", cursive; font-size: 29px; line-height: 1.15; color: var(--orange);
  }
  .date-block {
    position: absolute; left: 440px; top: 128px; padding-left: 14px;
    border-left: 3px solid var(--white); color: var(--white);
    font-weight: 900; font-size: 19px; line-height: 1.2;
  }
  .art { position: absolute; }
  .art.dove { left: 28px; top: 150px; width: 92px; height: 62px; border-radius: 50%;
    background: radial-gradient(ellipse, #ffffff 0%, #dcdde6 70%, rgba(220,221,230,0) 100%); }
  .art.animals { left: 120px; top: 232px; width: 480px; height: 180px; border-radius: 40px 40px 20px 20px;
    background: linear-gradient(90deg, #f3cfcd 0%, #e9c1bd 22%, #3b3336 38%, #c9a889 55%, #b8a79b 68%, #e3b66e 85%, #c98f4c 100%); }
  .info { position: absolute; left: 24px; top: 420px; width: 300px; font-size: 10.5px; line-height: 1.35; }
  .info h2 { color: var(--orange); font-size: 12.5px; font-weight: 900; line-height: 1.2; margin-bottom: 2px; }
  .info .group { padding-bottom: 5px; margin-bottom: 6px; border-bottom: 1px solid var(--rule); }
  .info .group:last-child { border-bottom: 0; margin-bottom: 0; }
  .dot { color: var(--orange); font-weight: 900; }
  .info strong { font-weight: 900; }
  .schedule { position: absolute; left: 350px; top: 428px; width: 256px; color: var(--white); }
  .schedule h2 { color: var(--orange); font-size: 15px; font-weight: 900; letter-spacing: 0.5px; margin-bottom: 6px; }
  .schedule ul { list-style: none; font-size: 12.5px; font-weight: 700; line-height: 1.5; }
  .schedule li { position: relative; padding-left: 14px; }
  .schedule li::before { content: ""; position: absolute; left: 0; top: 6px; width: 7px; height: 7px; border-radius: 50%; background: var(--orange); }
  .sponsors { position: absolute; left: 0; top: 738px; width: 618px; text-align: center;
    color: var(--muted); font-weight: 900; font-size: 34px; line-height: 1.2; letter-spacing: 1px; }
</style>
</head>
<body>
<div class="canvas">
  <article class="flyer">
    <div class="hero"></div>
    <div class="schedule-panel"></div>
    <div class="accent-stripe left"></div>
    <div class="accent-stripe right"></div>

    <h1 class="title"><span class="line-one">Corvel Heights</span><span class="line-two">Pet GALA</span></h1>
    <div class="art dove" role="img" aria-label="Photo of a white dove in flight"></div>
    <p class="tagline">(Fun for Animals In Rescue!)</p>
    <p class="date-block">SUNDAY,<br>August 12, 2018<br>1 to 4:30 p.m.</p>
    <div class="art animals" role="img" aria-label="Photo group of a pig, a goat, a bunny, a kitten and two dogs"></div>

    <section class="info">
      <div class="group">
        <h2>Animal Education &amp; Adoption Event featuring:</h2>
        <p><span class="dot">●</span> BK Pet Shelter &amp; Services Rabbits &amp; Mice <span class="dot">●</span> Hilltop Browsing Sheep <span class="dot">●</span> Thankful Hounds Haven <span class="dot">●</span> Featherwell Finches &amp; Larks <span class="dot">●</span> Comet Pup Haven <span class="dot">●</span> Marla’s Feline Haven <span class="dot">●</span> Marvel Pup Haven</p>
      </div>
      <div class="group">
        <p><strong>Special Guest from 1-3 p.m.<br>BeeBop - SF's 1st Therapy Pig!</strong><br>Instagram: @BEEBOP_BKHOG<br>Facebook: @BEEBOP THE HOG</p>
      </div>
      <div class="group">
        <h2>ACTIVITIES FOR KIDS</h2>
        <p>Dog &amp; Cat Toy Making with Greta Vossel Canine Coaching<br>Animal Mask Making with Tiny Crafters<br>Face-in-a-Hole Photo Fun with Hugo Marsh Canine Coaching</p>
      </div>
      <div class="group">
        <h2>BK PSS FREE Giveaway!</h2>
        <p>First 75 attending families receive a FREE PSS Doggie Bag containing a dog water bottle, food, shampoo, toy, treats and blinking dog collar light.</p>
      </div>
    </section>

    <section class="schedule">
      <h2>ANIMAL TAILS</h2>
      <ul>
        <li>1 pm Wendell’s Nook Storytime</li>
        <li>1:30 p.m. BeeBop the Therapy Pig</li>
        <li>1:45 pm “Tuft the Saved Hog”<br>Read by Author Marnie Oakhurst</li>
        <li>2 p.m. Wendell’s Nook Singalong</li>
        <li>2:30 p.m. Featherwell Finch Haven</li>
        <li>2:45 p.m. Quire Pages Storytime</li>
        <li>3 pm Browsing Sheep Refuge</li>
        <li>3:15 p.m. The Burrow Den Puppet Show</li>
        <li>3:45 pm BK PSS Officer Tamsin</li>
        <li>4 p.m. Wendell’s Nook Storytime</li>
      </ul>
    </section>

    <p class="sponsors">sponsoring logos</p>
  </article>
</div>
</body>
</html>
```